Bi-Lingual Trash and Recycle Sign

Hello,

Pretty straight forward. I have not been able to find the exact sign we need for a property with trash and recycle guidelines. I've found close, but not complete. We are looking to have metal 12x18 street sign type signs made to provide these instructions. Attached is a sample taken from the web. I want to be sure to avoid conflicting with them so looking for the same wording but in our own. I'd also like to include our company logo, also attached in vector in horizontal and vertical for inclusion.

```html
<!DOCTYPE html>
<html lang="en">
<head>
<meta charset="utf-8">
<title>Bilingual Recycling Sign</title>
<link href="https://fonts.googleapis.com/css2?family=Roboto+Condensed:wght@400;500;700;800&display=swap" rel="stylesheet">
<style>
  :root{
    --maroon:#6a1f36;
    --maroon-deep:#4d1528;
    --band-grey:#d8d8d8;
    --icon-fill:#e4e2e3;
    --icon-ring:#b9aeb2;
    --ink:#1f1f1f;
    --white:#ffffff;
    --backdrop:#eeeeee;
    --bin-light:#f3c928;
    --bin-dark:#d9a912;
  }
  *{box-sizing:border-box;margin:0;padding:0}
  html,body{width:1200px;height:900px;overflow:hidden;background:var(--backdrop)}
  body{font-family:"Roboto Condensed",Arial,sans-serif;position:relative}
  .sign{position:absolute;left:0;top:50px;width:1200px;height:800px;background:var(--white);overflow:hidden}
  .band-grey{position:absolute;left:0;top:273px;width:1200px;height:61px;background:var(--band-grey)}
  .band-maroon{position:absolute;left:0;top:334px;width:1200px;height:302px;
    background:linear-gradient(90deg,var(--maroon-deep) 0%,#3f0f20 45%,#3f0f20 55%,var(--maroon-deep) 100%)}
  .band-rule{position:absolute;left:0;top:636px;width:1200px;height:7px;background:var(--band-grey)}
  .col{position:absolute;width:440px;text-align:center}
  .col-en{left:-3px}
  .col-es{left:759px}
  .headline{position:absolute;left:0;width:100%;top:96px;font-size:62px;font-weight:800;color:var(--maroon);letter-spacing:.5px;line-height:1}
  .notice{position:absolute;left:0;width:100%;top:192px;font-size:26px;font-weight:700;color:var(--maroon);line-height:1.2}
  .col-es .notice{top:185px}
  .sort-title{position:absolute;left:0;width:100%;top:288px;font-size:26px;font-weight:500;color:var(--maroon);line-height:1}
  .materials-title{position:absolute;left:0;width:100%;top:362px;font-size:18px;font-weight:400;color:var(--white);letter-spacing:.3px}
  .materials{position:absolute;left:20px;top:404px;width:400px;display:grid;grid-template-columns:repeat(4,100px);row-gap:20px}
  .material{display:flex;flex-direction:column;align-items:center}
  .material-icon{width:64px;height:64px;border-radius:50%;background:var(--icon-fill);border:3px solid var(--icon-ring);display:flex;align-items:center;justify-content:center}
  .material-icon svg{width:38px;height:38px}
  .material-label{margin-top:12px;font-size:14px;color:var(--white);letter-spacing:.2px;white-space:nowrap}
  .closing{position:absolute;left:0;width:100%;top:680px;color:var(--maroon);font-weight:700;line-height:1.05}
  .col-es .closing{top:675px}
  .closing .small{display:block;font-size:25px}
  .closing .large{display:block;font-size:33px}
  .brand{position:absolute;left:486px;top:52px;display:flex;align-items:center;gap:8px;color:var(--ink);font-weight:700;font-size:27px}
  .brand-mark{width:18px;height:18px;background:var(--maroon)}
  .bin{position:absolute;left:432px;top:133px;width:346px;height:592px;border-radius:10px 10px 40px 40px;
    background:linear-gradient(90deg,var(--bin-dark),var(--bin-light) 45%,var(--bin-dark))}
  .url{position:absolute;left:406px;width:400px;text-align:center;top:746px;font-size:25px;font-weight:700;color:var(--maroon)}
  .icon-defs{position:absolute;width:0;height:0}
  .stroke{fill:none;stroke:var(--ink);stroke-width:2.2;stroke-linejoin:round;stroke-linecap:round}
</style>
</head>
<body>
<svg class="icon-defs" aria-hidden="true">
  <symbol id="i-glass" viewBox="0 0 40 40"><path class="stroke" d="M10 6h20v8a10 10 0 0 1-20 0z M20 24v9 M13 34h14"/></symbol>
  <symbol id="i-tin" viewBox="0 0 40 40"><path class="stroke" d="M11 6h18M11 34h18M13 6v28M27 6v28M13 11h14M13 29h14"/><ellipse class="stroke" cx="20" cy="20" rx="5" ry="3"/></symbol>
  <symbol id="i-alu" viewBox="0 0 40 40"><rect class="stroke" x="7" y="10" width="18" height="22" rx="2"/><path class="stroke" d="M17 8l14 3-4 20"/><text x="16" y="25" font-size="8" text-anchor="middle" font-family="Roboto Condensed,sans-serif">AU</text></symbol>
  <symbol id="i-plastic" viewBox="0 0 40 40"><path class="stroke" d="M9 34V16l3-4V7h4v5l3 4v18z M9 22h10 M23 34V22h10v12z M26 22v-4h4v4 M12 5h6"/></symbol>
  <symbol id="i-box" viewBox="0 0 40 40"><path class="stroke" d="M20 8l14 7-14 7-14-7z M6 15v11l14 7 14-7V15 M20 22v11 M6 15l-2 5 14 7 2-5 M34 15l2 5-14 7"/></symbol>
  <symbol id="i-paper" viewBox="0 0 40 40"><path class="stroke" d="M8 12l10-5 6 12-10 5z M16 18h12v16H16z M19 23h6M19 27h6M19 31h4"/></symbol>
  <symbol id="i-news" viewBox="0 0 40 40"><path class="stroke" d="M12 6h20v28H9V14h3z M12 14v20 M16 12h12M16 17h12M16 22h12M16 27h12"/></symbol>
  <symbol id="i-mag" viewBox="0 0 40 40"><path class="stroke" d="M6 9h13v23H6z M21 9h13v23H21z M9 14h7M9 19h7M9 24h7M24 14h7M24 19h7M24 24h7"/></symbol>
</svg>

<main class="sign">
  <div class="band-grey"></div>
  <div class="band-maroon"></div>
  <div class="band-rule"></div>

  <section class="col col-en" lang="en">
    <h1 class="headline">RECYCLE</h1>
    <p class="notice">NO PLASTIC BAGS<br>ACCEPTED</p>
    <h2 class="sort-title">SINGLE SORT RECYCLING</h2>
    <h3 class="materials-title">ACCEPTED MATERIALS</h3>
    <ul class="materials" style="list-style:none">
      <li class="material"><span class="material-icon"><svg><use href="#i-glass"/></svg></span><span class="material-label">GLASS</span></li>
      <li class="material"><span class="material-icon"><svg><use href="#i-tin"/></svg></span><span class="material-label">TIN</span></li>
      <li class="material"><span class="material-icon"><svg><use href="#i-alu"/></svg></span><span class="material-label">ALUMINUM</span></li>
      <li class="material"><span class="material-icon"><svg><use href="#i-plastic"/></svg></span><span class="material-label">PLASTIC (1-7)</span></li>
      <li class="material"><span class="material-icon"><svg><use href="#i-box"/></svg></span><span class="material-label">CARDBOARD</span></li>
      <li class="material"><span class="material-icon"><svg><use href="#i-paper"/></svg></span><span class="material-label">MIXED PAPER</span></li>
      <li class="material"><span class="material-icon"><svg><use href="#i-news"/></svg></span><span class="material-label">NEWSPAPERS</span></li>
      <li class="material"><span class="material-icon"><svg><use href="#i-mag"/></svg></span><span class="material-label">MAGAZINES</span></li>
    </ul>
    <p class="closing"><span class="small">ABSOLUTELY</span><span class="large">NO GARBAGE!</span></p>
  </section>

  <section class="col col-es" lang="es">
    <h1 class="headline">RECICLAR</h1>
    <p class="notice">NO SE ACEPTAN<br>BOLSAS PLÁSTICAS</p>
    <h2 class="sort-title">RECICLAJE DE CLASE ÚNICA</h2>
    <h3 class="materials-title">ÚNICO ORDENAR EL RECICLAJE</h3>
    <ul class="materials" style="list-style:none">
      <li class="material"><span class="material-icon"><svg><use href="#i-glass"/></svg></span><span class="material-label">VIDRIOS</span></li>
      <li class="material"><span class="material-icon"><svg><use href="#i-tin"/></svg></span><span class="material-label">HOJALATA</span></li>
      <li class="material"><span class="material-icon"><svg><use href="#i-alu"/></svg></span><span class="material-label">ALUMINIO</span></li>
      <li class="material"><span class="material-icon"><svg><use href="#i-plastic"/></svg></span><span class="material-label">PLÁSTICO (1-7)</span></li>
      <li class="material"><span class="material-icon"><svg><use href="#i-box"/></svg></span><span class="material-label">CARTÓN</span></li>
      <li class="material"><span class="material-icon"><svg><use href="#i-paper"/></svg></span><span class="material-label">PAPEL</span></li>
      <li class="material"><span class="material-icon"><svg><use href="#i-news"/></svg></span><span class="material-label">PERIÓDICOS</span></li>
      <li class="material"><span class="material-icon"><svg><use href="#i-mag"/></svg></span><span class="material-label">REVISTAS</span></li>
    </ul>
    <p class="closing"><span class="small">ABSOLUTAMENTE</span><span class="large">NINGUNA BASURA!</span></p>
  </section>

  <div class="brand"><span class="brand-mark"></span><span>HARWELL MANAGEMENT</span></div>
  <div class="bin" role="img" aria-label="Yellow wheeled recycling bin with a recycling symbol"></div>
  <p class="url">harwellhomes.com</p>
</main>
</body>
</html>
```